BUilding Fascia Signage

I got the logo, now, I want to design the Fascia Signage for my shop.
Fasica signage is 5565mm x 470mmH
Need idea how to put the logo, text, colour to the fascia signage.
need something catching.
can add more decorate line.
may try with Black background and white background

Design & Build

```html
<!DOCTYPE html>
<html lang="en">
<head>
<meta charset="utf-8">
<title>RNV Building Group – Fascia Sign</title>
<link rel="stylesheet" href="https://fonts.googleapis.com/css2?family=Poppins:wght@700;800&family=Exo+2:ital,wght@1,800&display=swap">
<style>
  :root {
    --backdrop: #999999;
    --sign-white: #ffffff;
    --ink: #0c0c0c;
    --brand-blue: #2f86f0;
  }
  html, body {
    margin: 0;
    padding: 0;
    width: 1200px;
    height: 778px;
    overflow: hidden;
    background: var(--backdrop);
  }
  .canvas {
    width: 1200px;
    height: 778px;
    display: flex;
    align-items: center;
    justify-content: center;
  }
  .fascia {
    width: 1140px;
    height: auto;
    display: block;
    box-shadow: 0 2px 6px rgba(0, 0, 0, 0.25);
  }
  .fascia-base { fill: var(--sign-white); }
  .band-black { fill: var(--ink); }
  .band-blue { fill: var(--brand-blue); }
  .rule-blue { stroke: var(--brand-blue); stroke-width: 2; }
  .brand-name {
    font-family: "Poppins", sans-serif;
    font-weight: 800;
    fill: var(--ink);
    font-size: 15px;
  }
  .brand-square { fill: var(--brand-blue); }
  .headline {
    font-family: "Poppins", sans-serif;
    font-weight: 700;
    font-size: 38px;
    fill: var(--ink);
  }
  .headline .accent { fill: var(--brand-blue); }
  .phone-number {
    font-family: "Exo 2", sans-serif;
    font-style: italic;
    font-weight: 800;
    font-size: 31px;
    fill: var(--sign-white);
    letter-spacing: 0.5px;
  }
  .phone-badge { fill: var(--sign-white); }
  .phone-glyph { fill: var(--brand-blue); }
</style>
</head>
<body>
<main class="canvas">
  <svg class="fascia" viewBox="0 0 1320 112" xmlns="http://www.w3.org/2000/svg" aria-label="Fascia sign for RNV Building Group">
    <rect class="fascia-base" x="0" y="0" width="1320" height="112"/>

    <!-- lower black band rising into phone panel -->
    <polygon class="band-black" points="138,112 160,86 1000,86 1045,56 1320,56 1320,112"/>
    <!-- blue accent along the rise -->
    <polygon class="band-blue" points="955,84 1000,54 1320,54 1320,47 1005,47 960,78 170,78 170,84"/>
    <line class="rule-blue" x1="170" y1="81" x2="965" y2="81"/>

    <!-- top-right dash strip -->
    <g class="dash-strip">
      <polygon class="band-black" points="1035,49 1041,41 1061,41 1055,49"/>
      <polygon class="band-blue" points="1059,49 1065,41 1085,41 1079,49"/>
      <polygon class="band-black" points="1083,49 1089,41 1109,41 1103,49"/>
      <polygon class="band-blue" points="1107,49 1113,41 1133,41 1127,49"/>
      <polygon class="band-black" points="1131,49 1137,41 1157,41 1151,49"/>
      <polygon class="band-blue" points="1155,49 1161,41 1181,41 1175,49"/>
      <polygon class="band-black" points="1179,49 1185,41 1205,41 1199,49"/>
      <polygon class="band-blue" points="1203,49 1209,41 1229,41 1223,49"/>
      <polygon class="band-black" points="1227,49 1233,41 1253,41 1247,49"/>
      <polygon class="band-blue" points="1251,49 1257,41 1277,41 1271,49"/>
      <polygon class="band-black" points="1275,49 1281,41 1301,41 1295,49"/>
      <polygon class="band-blue" points="1299,49 1305,41 1320,41 1320,49"/>
    </g>

    <!-- bottom-left dash strip -->
    <g class="dash-strip">
      <polygon class="band-blue" points="0,112 0,104 14,104 8,112"/>
      <polygon class="band-black" points="12,112 18,104 34,104 28,112"/>
      <polygon class="band-blue" points="32,112 38,104 54,104 48,112"/>
      <polygon class="band-black" points="52,112 58,104 74,104 68,112"/>
      <polygon class="band-blue" points="72,112 78,104 94,104 88,112"/>
      <polygon class="band-black" points="92,112 98,104 114,104 108,112"/>
      <polygon class="band-blue" points="112,112 118,104 134,104 128,112"/>
    </g>

    <!-- brand name -->
    <g class="brand">
      <rect class="brand-square" x="18" y="36" width="12" height="12"/>
      <text class="brand-name" x="36" y="46">RNV</text>
      <text class="brand-name" x="18" y="66">Building Group</text>
    </g>

    <!-- headline -->
    <text class="headline" x="170" y="58">Your Home <tspan class="accent">OUR HEART</tspan> Crafted to Amare</text>

    <!-- phone -->
    <g class="phone">
      <circle class="phone-badge" cx="1060" cy="78" r="11"/>
      <path class="phone-glyph" d="M1055,72 q2,-2 4,0 l2,3 q1,1.5 -0.5,2.5 l-1,0.8 q1.5,3 4,4 l0.8,-1 q1,-1.5 2.5,-0.5 l3,2 q2,2 0,4 q-3,3 -8,-1 q-5,-4 -7.5,-8 q-2,-4 0.7,-5.8z"/>
      <text class="phone-number" x="1078" y="90">0400 555 019</text>
    </g>
  </svg>
</main>
</body>
</html>
```